VESTARO EV

We need a business card design for a new Luxury golf cart Company Vestaro. We manufacture and sell high end golf carts. We would like to see designs that are high end. I have the logo so really need a nice clean look.

```html
<!DOCTYPE html>
<html lang="en">
<head>
<meta charset="utf-8">
<title>Vestaro EV — Business Card</title>
<link href="https://fonts.googleapis.com/css2?family=Montserrat:wght@400;500;700&display=swap" rel="stylesheet">
<style>
  :root{
    --page-bg:#d9d9d9;
    --card-bg:#ffffff;
    --card-back-bg:#f1f1f1;
    --brand-ink:#1c1c1c;
    --name-ink:#7a7a7a;
    --meta-ink:#8a8a8a;
    --address-ink:#4a4a4a;
    --shadow:rgba(0,0,0,.18);
  }
  *{box-sizing:border-box;margin:0;padding:0}
  html,body{width:1200px;height:1200px;overflow:hidden}
  body{
    background:var(--page-bg);
    font-family:"Montserrat",sans-serif;
    display:flex;flex-direction:column;align-items:center;justify-content:center;gap:60px;
  }
  .card{
    position:relative;width:880px;height:503px;border-radius:28px;
    box-shadow:0 10px 26px var(--shadow);
  }
  .card--front{background:var(--card-bg);display:flex;align-items:center;justify-content:center}
  .card--back{background:var(--card-back-bg)}
  .brand-name{
    font-weight:700;color:var(--brand-ink);letter-spacing:.08em;line-height:1;white-space:nowrap;
  }
  .card--front .brand-name{font-size:96px}
  .card--back .brand-name{position:absolute;top:50px;right:60px;font-size:52px}
  .holder{position:absolute;left:70px;bottom:62px}
  .holder__name{font-size:36px;font-weight:700;color:var(--name-ink)}
  .holder__role{font-size:22px;font-weight:400;color:var(--meta-ink);margin:6px 0 16px}
  .contact-list{list-style:none}
  .contact-list li{display:flex;align-items:center;gap:14px;font-size:24px;color:var(--meta-ink);margin-top:6px}
  .contact-list svg{width:20px;height:20px;fill:var(--meta-ink);flex:none}
  .address{
    position:absolute;right:60px;bottom:150px;text-align:right;font-style:normal;
    font-size:24px;font-weight:500;color:var(--address-ink);line-height:1.4;
  }
</style>
</head>
<body>
  <section class="card card--front" aria-label="Card front">
    <div class="brand-name">VESTARO</div>
  </section>

  <section class="card card--back" aria-label="Card back">
    <div class="brand-name">VESTARO</div>

    <div class="holder">
      <p class="holder__name">Everett Lane</p>
      <p class="holder__role">Founder &amp; Director</p>
      <ul class="contact-list">
        <li>
          <svg viewBox="0 0 24 24" aria-hidden="true"><path d="M6.6 10.8a15 15 0 0 0 6.6 6.6l2.2-2.2a1 1 0 0 1 1-.25 11.4 11.4 0 0 0 3.6.57 1 1 0 0 1 1 1V20a1 1 0 0 1-1 1A17 17 0 0 1 3 4a1 1 0 0 1 1-1h3.5a1 1 0 0 1 1 1c0 1.25.2 2.45.57 3.57a1 1 0 0 1-.25 1z"/></svg>
          555-014-2290
        </li>
        <li>
          <svg viewBox="0 0 24 24" aria-hidden="true"><path d="M3 5h18a1 1 0 0 1 1 1v12a1 1 0 0 1-1 1H3a1 1 0 0 1-1-1V6a1 1 0 0 1 1-1zm0 2.2V18h18V7.2l-9 6z"/><path d="M3 6l9 6 9-6z"/></svg>
          info@vestaro-ev.com
        </li>
        <li>
          <svg viewBox="0 0 24 24" aria-hidden="true"><path d="M12 2a10 10 0 1 0 0 20 10 10 0 0 0 0-20zm6.9 9h-3a15 15 0 0 0-1.3-5.6A8 8 0 0 1 18.9 11zM12 4.1c.9 1.2 1.8 3.6 1.9 6.9h-3.8c.1-3.3 1-5.7 1.9-6.9zM9.4 5.4A15 15 0 0 0 8.1 11h-3a8 8 0 0 1 4.3-5.6zM5.1 13h3a15 15 0 0 0 1.3 5.6A8 8 0 0 1 5.1 13zm6.9 6.9c-.9-1.2-1.8-3.6-1.9-6.9h3.8c-.1 3.3-1 5.7-1.9 6.9zm2.6-1.3a15 15 0 0 0 1.3-5.6h3a8 8 0 0 1-4.3 5.6z"/></svg>
          www.vestaro-ev.com
        </li>
      </ul>
    </div>

    <address class="address">
      1180 Harbor Point Way #12<br>
      Seabrook Bay, SC 29000
    </address>
  </section>
</body>
</html>
```